Veltrix Website

We need a website for a new Telecommunications company based in Australia. Our service is offered to people who are in the middle of moving properties as our major channel partners relocate renters and home owners. The website will outline the products we sell, which will include pricing as well as provide information for people who are in the middle of a move. Our client base will not come from any demographic, however 95% will be people renting properties and therefore most likely range in age from 18 and upwards. I would like to have an energetic feel to the website with a young theme. It needs full integration with Social Media, must be mobile centric as well, must include video as well as have chat options for visitors and be as interactive as possible . It should not be too cluttered as it needs to be clean and feel fresh. People who are moving are time poor and stressed (I am sure you have all moved!) and therefore our service needs to be complimentary and simple for them to engage with. We have a channel passing hot leads for this purpose, however we would like to market our services to others outside of this channel. We are offering most services such as home phone, internet and prepaid mobiles as unlimited services to make things simple and easy to commit to. Logo at this stage is Red, however we also need soothing colours on the site. I like the website layout of Plovara.com as an example, as it is clean and delivers the type of feel we are after. Your design does not have to mimic it, it just needs to give off the same feel.
Updates

Specific Competitors websites include the following:

http://www.brindlepath.com.au/
http://www.quarvelink.com.au/index.asp
http://morbanwire.com.au/
http://www.feltragrid.com.au/

Our site needs to be far more interactive than these.  Chat prompts once someone is on the site would be useful - asking "Are you ready to move?" "Do you want everything unlimited?" - click to chat, etc.

Hi Designers,

Could you please look at making the designs more Telecommunications focused.  Our primary focus is to move peoples phone services, so the Telco component and Broadband and internet is a key component.  The moving information is good, however none of the designs addresses the Telecommunications part, I want it clear that when someone comes to the site they can get a new fixed line, internet and pre paid mobile phone plan.

Thanks

Gus

Target Market(s)

People moving property who want to get their telecommunication and internet services connected at their new place.

Industry/Entity Type

Internet

Requirements
Must have
• Social Media
Video section
How to section
Pricing section
Moving information section
Useful links section
Live chat

```html
<!DOCTYPE html>
<html lang="en">
<head>
<meta charset="utf-8">
<title>Veltrix – Moving Home Telecommunications</title>
<link href="https://fonts.googleapis.com/css2?family=Arimo:wght@400;700&display=swap" rel="stylesheet">
<style>
:root{
  --red:#ed1c24;
  --red-dark:#c4141b;
  --ink:#222;
  --grey:#555;
  --muted:#8a8a8a;
  --line:#d6d6d6;
  --black:#000;
  --panel:#2b2b2b;
}
*{box-sizing:border-box;margin:0;padding:0}
html,body{width:1200px;height:964px;overflow:hidden;background:#fff}
body{position:relative;font-family:"Arimo",Arial,sans-serif;color:var(--ink)}
.abs{position:absolute}

/* header */
.site-header{left:0;top:0;width:1200px;height:128px;background:linear-gradient(#fafafa,#d8d8d8)}
.brand-mark{left:161px;top:12px;width:90px;height:90px;border-radius:50%;background:var(--red)}
.brand-name{left:161px;top:38px;width:90px;text-align:center;color:#fff;font-weight:700;font-size:22px}
.brand-url{left:147px;top:106px;font-size:11px;font-weight:700;color:var(--grey)}
.main-nav{left:330px;top:102px;display:flex;gap:0;font-size:13.5px;color:var(--grey)}
.main-nav span{margin-right:22px}
.main-nav .active{color:var(--red)}
.call-box{left:860px;top:30px;width:194px;text-align:center}
.call-number{font-size:16px;color:var(--red)}
.call-number b{color:var(--grey)}
.call-prompt{font-size:11.5px;color:var(--ink);line-height:15px;margin-top:3px}
.chat-button{left:903px;top:91px;width:133px;height:26px;border-radius:8px;background:linear-gradient(var(--red),var(--red-dark));color:#fff;font-weight:700;font-size:13px;display:flex;align-items:center;justify-content:center;gap:12px}
.header-rule{left:0;top:128px;width:1200px;height:8px;background:linear-gradient(90deg,#111,#444 50%,#111)}

/* hero */
.hero{left:0;top:143px;width:1200px;height:369px;background:var(--red)}
.hero-photo{left:144px;top:160px;width:640px;height:352px;background:linear-gradient(120deg,#e9e6e2,#d9cbb6 55%,#b98d5c);clip-path:polygon(0 0,470px 0,640px 100%,0 100%)}
.hero-title{left:740px;top:212px;width:326px;text-align:center;color:#fff;font-weight:700;font-size:29px;letter-spacing:2px;line-height:34px}
.hero-text{left:752px;top:308px;width:302px;text-align:center;font-size:13px;line-height:16px;color:#000}
.quote-button{left:824px;top:392px;width:157px;height:28px;border-radius:14px;background:linear-gradient(#444,#000);color:#fff;font-size:13.5px;display:flex;align-items:center;justify-content:center;gap:14px}
.slide-dots{left:684px;top:493px;display:flex;gap:4px}
.slide-dots i{width:9px;height:9px;border-radius:50%;background:#333}
.slide-dots i.on{background:var(--red)}

/* content */
.section-title{top:552px;font-size:16.5px;color:var(--grey)}
.feedback-list{left:145px;top:593px;width:240px}
.feedback-item{display:flex;gap:10px;height:46px;font-size:11px;line-height:13px;color:var(--grey)}
.feedback-item svg{flex:none;margin-top:1px}
.scroll-rail{width:1px;background:#bbb}
.button-red{height:21px;background:var(--red);color:#fff;font-size:12.5px;display:flex;align-items:center;justify-content:center;border-radius:2px}
.pin-btn{width:22px;height:22px;background:#e5e5e5;border-radius:2px;display:flex;align-items:center;justify-content:center}
.rule{height:1px;background:var(--line)}
.why-list{left:462px;top:593px;font-size:11px;color:var(--muted);letter-spacing:.5px}
.why-list li{list-style:none;display:flex;align-items:center;gap:8px;height:23px}
.why-text{left:462px;top:735px;width:220px;font-size:11px;line-height:15px;color:var(--muted);letter-spacing:.3px}

/* video */
.video-player{left:789px;top:556px;width:267px;height:194px;background:var(--panel);border:1px solid #111}
.video-label{left:6px;top:3px;font-size:6px;font-weight:700;color:#ddd}
.video-screen{left:5px;top:21px;width:255px;height:138px;background:#cfcfcf;border:1px solid #555}
.video-mark{left:80px;top:18px;width:92px;height:92px;border-radius:50%;background:var(--red)}
.video-name{left:80px;top:52px;width:92px;text-align:center;color:#fff;font-weight:700;font-size:19px}
.video-url{left:0;top:114px;width:255px;text-align:center;font-size:11px;font-weight:700;color:#333}
.video-controls{left:8px;top:172px;width:250px;display:flex;align-items:center;gap:4px;font-size:6px;color:#ccc}
.video-caption{left:789px;top:766px;width:270px;font-size:11px;line-height:15px;color:var(--muted);letter-spacing:.2px}
.video-link{left:789px;top:821px;font-size:10px;color:var(--red)}

/* footer */
.newsletter{left:0;top:872px;width:1200px;height:40px;background:var(--red)}
.mail-tab{left:145px;top:872px;width:53px;height:40px;background:linear-gradient(#444,#111);display:flex;align-items:center;justify-content:center}
.newsletter-text{left:206px;top:890px;font-size:12px;color:#fff}
.signup-label{left:688px;top:892px;font-size:12px;color:#000}
.email-field{left:830px;top:885px;width:164px;height:21px;background:#fff;border:1px solid #ccc;font-size:9px;color:var(--grey);padding:6px 0 0 7px}
.signup-button{left:998px;top:885px;width:58px;height:20px;background:linear-gradient(#444,#000);color:#fff;font-size:12px;display:flex;align-items:center;justify-content:center;border-radius:2px}
.site-footer{left:0;top:916px;width:1200px;height:48px;background:var(--black)}
.copyright{left:145px;top:934px;font-size:12px;color:#fff}
.copyright b{color:var(--red)}
.social-links{left:967px;top:926px;display:flex;gap:5px}
.social-links span{width:26px;height:26px;border-radius:4px}
</style>
</head>
<body>

<header class="site-header abs"></header>
<div class="brand-mark abs"></div>
<div class="brand-name abs">Veltrix</div>
<div class="brand-url abs">www.veltrix.com.au</div>
<nav class="main-nav abs">
  <span class="active">Home</span><span>About Us</span><span>Why choose Us</span><span>Pricing</span><span>Moving Home</span><span>Contact Us</span>
</nav>
<div class="call-box abs">
  <div class="call-number">Call Us # <b>155-402-718-9</b></div>
  <div class="call-prompt">Are you ready to move?<br>Do you want everything unlimited?</div>
</div>
<div class="chat-button abs">Click to Chat
  <svg width="11" height="12" viewBox="0 0 11 12"><path d="M0 0L11 6L0 12Z" fill="#fff"/></svg></div>
<div class="header-rule abs"></div>

<section class="hero abs"></section>
<div class="hero-photo abs" role="img" aria-label="Young woman on the phone with a laptop among moving boxes"></div>
<h1 class="hero-title abs">Lorem ipsum dolor sit amet</h1>
<p class="hero-text abs">Lorem ipsum dolor sit amet, consectetur adipiscing elit. Etiam metus lectus, bibendum vel viverra vitae, Quisque vitae hendrerit lacus.Etiam mollis erat eget dui vulputate varius.</p>
<div class="quote-button abs">Get Free Qoute
  <svg width="10" height="11" viewBox="0 0 10 11"><path d="M0 0L10 5.5L0 11Z" fill="#fff"/></svg></div>
<div class="slide-dots abs"><i></i><i></i><i></i><i class="on"></i></div>

<!-- customer feedback -->
<h2 class="section-title abs" style="left:145px;font-weight:400">Customer Feedback?</h2>
<div class="feedback-list abs">
  <div class="feedback-item"><svg width="20" height="24" viewBox="0 0 20 24"><rect x="0" y="4" width="20" height="20" fill="#666"/><rect x="4" y="0" width="2" height="6" fill="#666"/><rect x="14" y="0" width="2" height="6" fill="#666"/><path d="M3 10h14v11H3z" fill="#fff"/><path d="M3 13.5h14M3 17h14M6.5 10v11M10 10v11M13.5 10v11" stroke="#666"/></svg><span>Lorem ipsum dolor sit amet, consectetur adipiscing elit.</span></div>
  <div class="feedback-item"><svg width="20" height="24" viewBox="0 0 20 24"><rect x="0" y="4" width="20" height="20" fill="#666"/><rect x="4" y="0" width="2" height="6" fill="#666"/><rect x="14" y="0" width="2" height="6" fill="#666"/><path d="M3 10h14v11H3z" fill="#fff"/><path d="M3 13.5h14M3 17h14M6.5 10v11M10 10v11M13.5 10v11" stroke="#666"/></svg><span>Lorem ipsum dolor sit amet, consectetur adipiscing elit.</span></div>
  <div class="feedback-item"><svg width="20" height="24" viewBox="0 0 20 24"><rect x="0" y="4" width="20" height="20" fill="#666"/><rect x="4" y="0" width="2" height="6" fill="#666"/><rect x="14" y="0" width="2" height="6" fill="#666"/><path d="M3 10h14v11H3z" fill="#fff"/><path d="M3 13.5h14M3 17h14M6.5 10v11M10 10v11M13.5 10v11" stroke="#666"/></svg><span>Lorem ipsum dolor sit amet, consectetur adipiscing elit.</span></div>
  <div class="feedback-item"><svg width="20" height="24" viewBox="0 0 20 24"><rect x="0" y="4" width="20" height="20" fill="#666"/><rect x="4" y="0" width="2" height="6" fill="#666"/><rect x="14" y="0" width="2" height="6" fill="#666"/><path d="M3 10h14v11H3z" fill="#fff"/><path d="M3 13.5h14M3 17h14M6.5 10v11M10 10v11M13.5 10v11" stroke="#666"/></svg><span>Lorem ipsum dolor sit amet, consectetur adipiscing elit.</span></div>
  <div class="feedback-item"><svg width="20" height="24" viewBox="0 0 20 24"><rect x="0" y="4" width="20" height="20" fill="#666"/><rect x="4" y="0" width="2" height="6" fill="#666"/><rect x="14" y="0" width="2" height="6" fill="#666"/><path d="M3 10h14v11H3z" fill="#fff"/><path d="M3 13.5h14M3 17h14M6.5 10v11M10 10v11M13.5 10v11" stroke="#666"/></svg><span>Lorem ipsum dolor sit amet, consectetur adipiscing elit.</span></div>
</div>
<div class="abs" style="left:391px;top:589px;width:10px;height:8px;background:#ddd;border:1px solid #bbb"></div>
<div class="scroll-rail abs" style="left:396px;top:600px;height:205px"></div>
<div class="button-red abs" style="left:146px;top:809px;width:78px">Previous</div>
<div class="button-red abs" style="left:227px;top:809px;width:46px">Next</div>
<div class="pin-btn abs" style="left:385px;top:806px"><svg width="10" height="13" viewBox="0 0 10 13"><path d="M5 0a5 5 0 0 1 5 5c0 3-5 8-5 8S0 8 0 5a5 5 0 0 1 5-5z" fill="#111"/><circle cx="5" cy="5" r="1.8" fill="#e5e5e5"/></svg></div>
<div class="rule abs" style="left:145px;top:838px;width:263px"></div>

<!-- why choose us -->
<h2 class="section-title abs" style="left:462px;font-weight:400">Why Choose Us?</h2>
<ul class="why-list abs">
  <li><svg width="14" height="12" viewBox="0 0 14 12"><path d="M1 6l4 4L13 1" stroke="#ed1c24" stroke-width="2.5" fill="none"/></svg>Quisque pulvinar egestas neque.</li>
  <li><svg width="14" height="12" viewBox="0 0 14 12"><path d="M1 6l4 4L13 1" stroke="#ed1c24" stroke-width="2.5" fill="none"/></svg>Lorem ipsum dolor sit amet.</li>
  <li><svg width="14" height="12" viewBox="0 0 14 12"><path d="M1 6l4 4L13 1" stroke="#ed1c24" stroke-width="2.5" fill="none"/></svg>Quisque pulvinar egestas neque.</li>
  <li><svg width="14" height="12" viewBox="0 0 14 12"><path d="M1 6l4 4L13 1" stroke="#ed1c24" stroke-width="2.5" fill="none"/></svg>Lorem ipsum dolor sit amet.</li>
  <li><svg width="14" height="12" viewBox="0 0 14 12"><path d="M1 6l4 4L13 1" stroke="#ed1c24" stroke-width="2.5" fill="none"/></svg>Quisque pulvinar egestas neque.</li>
</ul>
<div class="rule abs" style="left:462px;top:725px;width:262px"></div>
<p class="why-text abs">Lorem ipsum dolor sit amet, consectetuer adipiscing elit, sed diam nonummy nibh euismod tincidunt ut laoreet dolore magna aliquam erat volutpat.</p>
<div class="abs" style="left:704px;top:739px;width:10px;height:8px;background:#ddd;border:1px solid #bbb"></div>
<div class="scroll-rail abs" style="left:709px;top:750px;height:50px"></div>
<div class="button-red abs" style="left:461px;top:809px;width:79px">View Ditale</div>
<div class="pin-btn abs" style="left:699px;top:808px"><svg width="10" height="13" viewBox="0 0 10 13"><path d="M5 0a5 5 0 0 1 5 5c0 3-5 8-5 8S0 8 0 5a5 5 0 0 1 5-5z" fill="#111"/><circle cx="5" cy="5" r="1.8" fill="#e5e5e5"/></svg></div>
<div class="rule abs" style="left:460px;top:839px;width:262px"></div>

<!-- featured video -->
<div class="video-player abs">
  <div class="video-label abs">Playing video</div>
  <div class="video-screen abs">
    <div class="video-mark abs"></div>
    <div class="video-name abs">Veltrix</div>
    <div class="video-url abs">www.veltrix.com.au</div>
  </div>
  <div class="video-controls abs">
    <svg width="46" height="18" viewBox="0 0 46 18"><circle cx="4" cy="9" r="4" fill="#ccc"/><circle cx="22" cy="9" r="8.5" fill="#ddd"/><path d="M19 5l7 4-7 4z" fill="#222"/><circle cx="40" cy="9" r="4" fill="#ccc"/></svg>
    <span style="margin-left:auto">00:00 / 00:00</span>
    <svg width="42" height="10" viewBox="0 0 42 10"><path d="M0 9L26 2V9Z" fill="#bbb"/><rect x="32" y="2" width="8" height="6" fill="#bbb"/></svg>
  </div>
</div>
<p class="video-caption abs">Lorem ipsum dolor sit amet, consectetuer adipiscing elit, sed diam nonummy nibh euismod tincidunt ut laoreet dolore magna aliquam erat volutpat.</p>
<div class="video-link abs">Featured video</div>
<div class="rule abs" style="left:789px;top:838px;width:267px"></div>

<!-- newsletter & footer -->
<section class="newsletter abs"></section>
<div class="mail-tab abs"><svg width="20" height="14" viewBox="0 0 20 14"><rect x=".5" y=".5" width="19" height="13" fill="#fff"/><path d="M.5.5L10 8 19.5.5" stroke="#333" fill="none"/></svg></div>
<div class="newsletter-text abs">Join Now For Our Newletter</div>
<div class="signup-label abs">Get the latest from Nuvora</div>
<svg class="abs" style="left:974px;top:858px" width="58" height="26" viewBox="0 0 58 26"><path d="M56 14C46 4 30 4 12 16" stroke="#222" stroke-width="2.5" fill="none"/><path d="M4 22L18 19 10 10Z" fill="#222"/></svg>
<div class="email-field abs">Your email address</div>
<div class="signup-button abs">Sign up</div>
<footer class="site-footer abs"></footer>
<div class="copyright abs">Copyright &copy; 2012 <b>VELTRIX</b> . All Rights Reserved</div>
<div class="social-links abs">
  <span style="background:#4fb0d8" aria-label="Social link"></span>
  <span style="background:#f07a22" aria-label="Feed link"></span>
  <span style="background:#4a6eaa" aria-label="Social link"></span>
</div>

</body>
</html>
```